'Ormel Property Development' Business Card

Business Card Features:

High Quality (potentially textured) thick card - preference is white textured card

Logo (supplied)

We plan to use the vertical logo as the main logo. But i am happy for people to use either if they find it works better for the design of the card.

The building icon and also the insert to the 'E' is in a metallic finish, i think this should be finished in a metallic embossed or raised style.
Updates

Please note i have attached both a horizontal and Vertical Logo for your reference. We plan to use the vertical logo as the main logo. But i am happy for people to use either if they find it works better for the design of the card.

Please note i am considering having the cards made on stainless steel. This introduces the option of having cut outs in the card and etching or printing for the design. If you have a good concept for this please submit.

http://www.tinquarry.example/black-metal-cards# this is a site that makes the metal cards to offer some direction . . . . Please note i am basic the selection o the best design, if that means normal print cards on paper then this is what i will choose. But there are some great options with the metal. Thanks.

Industry/Entity Type

Building

Requirements
Must have
• Helvetica font to details side of card - logo as supplied to opposite side.

Card Details:

Darrow Pketts
Managing Director

+61 487 263 518
+61 3 6172 4809

PO Box 73
Bentleigh, VIC 3024

darrow@ormel.example

www.ormel.example

```html
<!DOCTYPE html>
<html lang="en">
<head>
<meta charset="utf-8">
<title>Ormel Property Development – Business Card</title>
<link rel="stylesheet" href="https://fonts.googleapis.com/css2?family=Open+Sans:wght@400;600;700&display=swap">
<style>
  :root {
    --backdrop: #d9d4cc;
    --metal-dark: #0d0d0d;
    --metal-mid: #262626;
    --metal-light: #3a3a3a;
    --ink-light: #f2f2f2;
    --ink-soft: #cfcfcf;
    --silver: #c9c9c9;
    --band-grey: #6b6d6e;
    --line-grey: #a9abac;
    --divider: #5a5a5a;
  }
  * { margin: 0; padding: 0; box-sizing: border-box; }
  html, body {
    width: 1200px; height: 1151px; overflow: hidden;
    background: var(--backdrop);
    font-family: "Open Sans", Helvetica, Arial, sans-serif;
  }
  .card {
    position: absolute;
    width: 901px; height: 514px;
    overflow: hidden;
    background:
      radial-gradient(ellipse at 55% 40%, var(--metal-light) 0%, var(--metal-mid) 45%, var(--metal-dark) 100%);
    box-shadow: 0 3px 10px rgba(0,0,0,.35);
  }
  .card--front { left: 31px; top: 45px; }
  .card--back  { left: 258px; top: 598px; }

  /* front: brand block */
  .brand {
    position: absolute; left: 36px; top: 150px; width: 300px;
    color: var(--silver);
  }
  .brand__name {
    font-size: 86px; font-weight: 600; letter-spacing: 4px; line-height: 1;
  }
  .brand__tagline {
    margin-top: 12px; font-size: 15px; font-weight: 600;
    letter-spacing: 1.2px; color: var(--silver);
  }

  .divider {
    position: absolute; left: 563px; top: 105px;
    width: 2px; height: 240px; background: var(--divider);
  }
  .contact { position: absolute; left: 581px; top: 106px; color: var(--ink-light); }
  .contact__name { font-size: 27px; font-weight: 700; color: var(--ink-soft); line-height: 1.2; }
  .contact__role { font-size: 20px; color: var(--ink-soft); margin-top: 2px; }
  .contact__list { list-style: none; margin-top: 32px; }
  .contact__item {
    display: flex; align-items: center; gap: 6px;
    font-size: 20px; height: 48px;
  }
  .icon { width: 20px; height: 20px; fill: var(--ink-light); flex: none; }

  .address {
    position: absolute; left: 30px; top: 424px;
    display: flex; align-items: center; gap: 6px;
    font-size: 21px; color: var(--ink-light);
  }
  .footer-band { position: absolute; left: 0; bottom: 0; width: 901px; height: 80px; }
  .web {
    position: absolute; right: 24px; bottom: 16px;
    font-size: 24px; letter-spacing: 4px; color: var(--ink-light);
  }

  /* back */
  .back-brand {
    position: absolute; left: 0; right: 0; top: 150px; text-align: center;
    font-size: 110px; font-weight: 600; letter-spacing: 8px; color: var(--silver);
  }
  .back-web {
    position: absolute; left: 0; right: 0; top: 430px; text-align: center;
    font-size: 26px; letter-spacing: 5px; color: var(--ink-light);
  }
</style>
</head>
<body>

<section class="card card--front">
  <div class="brand">
    <div class="brand__name">ORMEL</div>
    <div class="brand__tagline">Property Development</div>
  </div>

  <div class="divider"></div>

  <div class="contact">
    <div class="contact__name">Darrow Pketts</div>
    <div class="contact__role">Managing Director</div>
    <ul class="contact__list">
      <li class="contact__item">
        <svg class="icon" viewBox="0 0 24 24"><path d="M6.6 10.8a15 15 0 0 0 6.6 6.6l2.2-2.2a1 1 0 0 1 1-.25 11.4 11.4 0 0 0 3.6.57 1 1 0 0 1 1 1V20a1 1 0 0 1-1 1A17 17 0 0 1 3 4a1 1 0 0 1 1-1h3.5a1 1 0 0 1 1 1c0 1.25.2 2.45.57 3.57a1 1 0 0 1-.25 1z"/></svg>
        048-726-3518
      </li>
      <li class="contact__item">
        <svg class="icon" viewBox="0 0 24 24"><path d="M6.6 10.8a15 15 0 0 0 6.6 6.6l2.2-2.2a1 1 0 0 1 1-.25 11.4 11.4 0 0 0 3.6.57 1 1 0 0 1 1 1V20a1 1 0 0 1-1 1A17 17 0 0 1 3 4a1 1 0 0 1 1-1h3.5a1 1 0 0 1 1 1c0 1.25.2 2.45.57 3.57a1 1 0 0 1-.25 1z"/></svg>
        1800-555-014(TF)
      </li>
      <li class="contact__item">
        <svg class="icon" viewBox="0 0 24 24"><path d="M3 5h18a1 1 0 0 1 1 1v12a1 1 0 0 1-1 1H3a1 1 0 0 1-1-1V6a1 1 0 0 1 1-1zm0 2v.5l9 5.5 9-5.5V7l-9 5.5z"/></svg>
        darrow@ormel.example
      </li>
    </ul>
  </div>

  <div class="address">
    <svg class="icon" viewBox="0 0 24 24"><path d="M12 2a7 7 0 0 1 7 7c0 5-7 13-7 13S5 14 5 9a7 7 0 0 1 7-7zm0 4.5A2.5 2.5 0 1 0 12 11.5 2.5 2.5 0 0 0 12 6.5z"/></svg>
    PO Box 73 Bentleigh, VIC 3024
  </div>

  <svg class="footer-band" viewBox="0 0 901 80" preserveAspectRatio="none">
    <rect x="0" y="36" width="560" height="12" fill="var(--line-grey)"/>
    <path d="M520 80 C 540 30, 560 14, 610 12 L 901 12 L 901 80 Z" fill="var(--band-grey)"/>
  </svg>
  <div class="web">www.ormel.example</div>
</section>

<section class="card card--back">
  <div class="back-brand">ORMEL</div>
  <div class="back-web">www.ormel.example</div>
</section>

</body>
</html>
```